4D Hush Little Nest Luxury Ultrasound Billboard

Design a HIGH-END, MODERN billboard for my private prenatal ultrasound studio, 4D Hush Little Nest, located in Pace, Florida.
This billboard will be viewed by drivers traveling at highway speeds, so it must be extremely clean, simple, and readable within 6 seconds.
About My Business
4D Hush Little Nest is a private prenatal ultrasound studio specializing in:
Highest technology 4D/HD Ultrasounds
Early Gender Determination
Pregnancy Confirmation
I have been serving families for nearly 10 years and is known for creating a memorable experience, not just an ultrasound appointment.
Design Style
I DO NOT want:
Flowers
Leaves
Swirls
Glitter
Hearts everywhere
Busy backgrounds
Generic maternity stock graphics
I DO want:
Modern
Luxury
Upscale
Clean
Professional
Eye-catching
Premium medical spa feel
Colors
Use colors from my logo:
LOGO Green ( or a deep green)
Black
White
Soft Gold accents
Images:
Incorporate my professional headshot in a clean, modern way, logo, and the ultrasound images
Text
Keep wording minimal.
Primary Headline ( OPEN TO IDEAS) :
EXAMPLES ( WOULD RATHER SOMETHING MORE CATCHY)
" ADVANCED IMAGING. UNFORGETTABLE MOMENTS"
"MEET YOUR BABY BEFORE BIRTH"
Under headline:
4D Ultrasound • Early Gender • Pregnancy Confirmation
Business Name:
4D Hush Little Nest
Private Prenatal Ultrasound Studio
Phone Number:
850-471-3905
Important
This billboard must be readable in 5–6 seconds from a moving vehicle.
Less text is better.
The phone number and business name must be visible from a distance.
The design should feel like a premium brand that immediately tells expecting parents:
“This is where I go to see my baby.”
Files Provided
Official logo
Headshot
Ultrasound images
Don’t make this look like a medical office billboard.
Make it look like a luxury baby experience billboard. That’s what separates 4D Hush Little Nest from hospitals, OB offices, and all the new studios popping up around you. The emotional connection is what gets moms to book. ❤️
Billboard Size - 10.6” x 36”

```html
<!DOCTYPE html>
<html lang="en">
<head>
<meta charset="utf-8">
<title>4D Hush Little Nest Billboard</title>
<link rel="stylesheet" href="https://fonts.googleapis.com/css2?family=Bebas+Neue&family=Montserrat:wght@800;900&display=swap">
<style>
  :root {
    --backdrop: #8a8a8a;
    --ink: #000000;
    --paper: #ffffff;
    --gold: #c9a03c;
    --gold-deep: #b08a34;
    --logo-green: #5d6b66;
    --dress: #efb126;
  }
  * { margin: 0; padding: 0; box-sizing: border-box; }
  html, body { width: 1200px; height: 605px; overflow: hidden; background: var(--backdrop); }
  .billboard {
    position: absolute; left: 48px; top: 142px;
    width: 1104px; height: 321px;
    background: var(--paper);
    overflow: hidden;
    box-shadow: 0 4px 16px rgba(0,0,0,.25);
  }
  .headline-band { position: absolute; left: 0; top: 0; width: 100%; height: 156px; background: var(--ink); }
  .brand-frame {
    position: absolute; left: 36px; top: 29px; width: 221px; height: 109px;
    border: 2px solid var(--logo-green); border-radius: 10px;
    display: flex; align-items: center; justify-content: center; gap: 8px;
  }
  .brand-dot { width: 12px; height: 12px; border-radius: 50%; background: var(--gold); }
  .brand-name {
    font-family: "Montserrat", sans-serif; font-weight: 800; font-size: 19px;
    color: var(--gold); line-height: 1.05; text-align: left;
  }
  .headline {
    position: absolute; left: 332px; top: 26px; z-index: 3;
    font-family: "Montserrat", sans-serif; font-weight: 900;
  }
  .headline .line-gold {
    display: block; color: var(--gold);
    font-size: 60px; line-height: 56px; letter-spacing: -2px;
  }
  .headline .line-white {
    display: block; color: var(--paper);
    font-size: 62px; line-height: 58px; letter-spacing: -0.5px;
  }
  .scan-print {
    position: absolute; left: 850px; top: 42px; width: 106px; height: 106px; z-index: 2;
    background: var(--paper); transform: rotate(-13deg); padding: 8px;
  }
  .scan-print .scan { width: 100%; height: 100%; background: linear-gradient(135deg, #3a1c14, #a8644e 45%, #6b3526 60%, #c07a60); }
  .pin { position: absolute; left: 902px; top: 30px; width: 9px; height: 9px; border-radius: 50%; background: #d9252a; z-index: 4; }
  .services {
    position: absolute; left: 0; top: 156px; width: 923px; height: 64px;
    background: var(--gold); display: flex; list-style: none;
  }
  .service {
    display: flex; align-items: center; gap: 8px;
    font-family: "Bebas Neue", sans-serif; font-size: 38px; color: var(--paper);
    padding-top: 4px;
  }
  .service::before {
    content: ""; width: 13px; height: 13px; border-radius: 50%;
    background: #3d3d3d; flex: none; margin-top: -4px;
  }
  .service-ultrasound { padding-left: 34px; width: 273px; }
  .service-gender { background: var(--gold-deep); padding-left: 18px; width: 236px; }
  .service-confirm { padding-left: 18px; }
  .studio-line {
    position: absolute; left: 39px; top: 232px;
    font-family: "Bebas Neue", sans-serif; font-size: 37px; line-height: 30px; color: var(--ink);
  }
  .divider { position: absolute; left: 311px; top: 237px; width: 2px; height: 59px; background: var(--ink); }
  .phone {
    position: absolute; left: 326px; top: 226px;
    font-family: "Montserrat", sans-serif; font-weight: 900; font-size: 76px;
    line-height: 80px; color: var(--ink); letter-spacing: -1px;
  }
  .mother-photo {
    position: absolute; left: 922px; top: 0; width: 182px; height: 321px; z-index: 1;
    background: linear-gradient(180deg, #c99672 0%, var(--dress) 22%, #e6a41d 70%, var(--dress) 100%);
    border-radius: 60px 40px 0 0;
  }
</style>
</head>
<body>
  <main class="billboard">
    <section class="headline-band">
      <div class="brand-frame">
        <span class="brand-dot"></span>
        <span class="brand-name">4D Hush<br>Little Nest</span>
      </div>
      <h1 class="headline">
        <span class="line-gold">MEET YOUR BABY</span>
        <span class="line-white">BEFORE BIRTH</span>
      </h1>
    </section>
    <div class="scan-print"><div class="scan" role="img" aria-label="3D ultrasound image of twin babies"></div></div>
    <span class="pin"></span>
    <ul class="services">
      <li class="service service-ultrasound">4D Ultrasound</li>
      <li class="service service-gender">Early Gender</li>
      <li class="service service-confirm">Pregnancy Confirmation</li>
    </ul>
    <p class="studio-line">PRIVATE PRENATAL<br>ULTRASOUND STUDIO</p>
    <span class="divider"></span>
    <p class="phone">850-471-3905</p>
    <div class="mother-photo" role="img" aria-label="Photo of a pregnant woman in a yellow dress holding a card with a heart"></div>
  </main>
</body>
</html>
```